Companybrochure for Consulting & Financing Firm

I need to have a Company Brochure asap for our company. We have a website that describes what we do, but we need also a brochure, that can be sent by PDF of eventually be printed as well.

The brochure should be short but nice and appealing to the customers.

We provide professional management consulting and help our customers to get finance for very diferent projects. Our business has a lot to do with personal relations, but also we are very professional in the way we work and how develop the solutions for our clients. Our clients are mainly government-owned firm, but also private trading companies and wealthy private investors.

Our customers are mainly in Latin America, but the company is headquater is in Switzerland. We are opening offices in Panama and Caracas, this should be easaly be adabtable later.

Please have a look at our website www.valtorhaus.ch. In the brochure, we would segment our services in 1.) Project Developments 2.) Management Conulting 3.) Investment Management and 4.) Finance Solutions.

Also do have a look at www.valtorhaus.ch
(Click E for the English version)
Updates

I managed to put the Mock-Up to the Website.
It is actually not really a mock-up, it is a version I have designed myself.
Well as I am not a designer, I hope you can make it much better.
The content however is what I would put in any other design as well.

Target Market(s)

Top Management, Investors, Entrepreneurs, Government Officials

Industry/Entity Type

Management Consulting

Requirements
Must have
• Design should reflect this image elements:

We are entrepreneurs.
We are comitted to get things done.
We work closely with the client side by side.
We are a professional partner.
We are not afraid of delivering unconventional solutions.
We look at the problem from various angles.
We analyse, develop solutions and implent results.
Should not have
• Typical US-American style elements. We do not want to give the impression of being a US company.

We do not want to appear to be neo-liberal. We are a politically neutral professional consulting firm.

```html
<!DOCTYPE html>
<html lang="en">
<head>
<meta charset="utf-8">
<title>Valtorhaus AG – Company Profile</title>
<link href="https://fonts.googleapis.com/css2?family=Arimo:wght@400;700&display=swap" rel="stylesheet">
<style>
  :root {
    --navy: #22406f;
    --mist: #e8e4e5;
    --paper: #ffffff;
    --ink: #0d0d0d;
  }
  html, body {
    margin: 0;
    padding: 0;
    overflow: hidden;
    background: var(--paper);
  }
  .brochure {
    position: relative;
    width: 1200px;
    height: 729px;
    overflow: hidden;
    font-family: "Arimo", Arial, sans-serif;
    background: var(--paper);
  }
  .backdrop {
    position: absolute;
    inset: 0;
  }
  .block {
    position: absolute;
    margin: 0;
    white-space: nowrap;
  }
  .motto-small {
    left: 18px;
    top: 40px;
    font-size: 17px;
    font-weight: 700;
    color: var(--navy);
  }
  .values {
    left: 18px;
    top: 90px;
    font-size: 18px;
    line-height: 23px;
    color: var(--navy);
  }
  .registration {
    left: 19px;
    top: 298px;
    font-size: 15.5px;
    color: var(--navy);
  }
  .contact {
    font-size: 15.5px;
    line-height: 20px;
    color: var(--paper);
  }
  .contact-address { left: 18px; top: 516px; }
  .contact-lines { left: 396px; top: 516px; }
  .contact-web { left: 193px; top: 641px; }
  .company-name {
    left: 659px;
    top: 64px;
    font-size: 33px;
    font-weight: 700;
    color: var(--paper);
  }
  .motto-large {
    left: 662px;
    top: 436px;
    font-size: 25px;
    font-weight: 700;
    color: var(--navy);
  }
  .intro {
    left: 661px;
    top: 518px;
    font-size: 18px;
    line-height: 23px;
    color: var(--ink);
  }
  .services {
    left: 657px;
    top: 580px;
    padding: 0;
    list-style: none;
    font-size: 18px;
    line-height: 22.6px;
    font-weight: 700;
    color: var(--ink);
  }
  .profile-label {
    left: 973px;
    top: 643px;
    font-size: 18px;
    font-weight: 700;
    color: var(--paper);
    letter-spacing: 0.2px;
  }
</style>
</head>
<body>
<main class="brochure">
  <svg class="backdrop" width="1200" height="729" viewBox="0 0 1200 729" aria-hidden="true">
    <rect class="panel-left-top" x="0" y="0" width="599" height="443" fill="var(--mist)"/>
    <polygon class="wedge-left" points="0,321 599,443 0,443" fill="var(--paper)"/>
    <rect class="panel-left-bottom" x="0" y="443" width="599" height="286" fill="var(--navy)"/>
    <polygon class="panel-right-top" points="599,0 1200,0 1200,140 599,443" fill="var(--navy)"/>
    <polygon class="panel-right-bottom" points="599,443 815,335 1200,625 1200,729 599,729" fill="var(--mist)"/>
    <line class="accent-line" x1="599" y1="181" x2="815" y2="335" stroke="var(--paper)" stroke-width="1.3"/>
    <line class="accent-line" x1="803" y1="331" x2="1200" y2="137" stroke="var(--paper)" stroke-width="1.3"/>
    <line class="accent-line" x1="830" y1="342" x2="1200" y2="620" stroke="var(--paper)" stroke-width="3"/>
    <line class="label-rule" x1="952" y1="637" x2="1200" y2="637" stroke="var(--paper)" stroke-width="1.3"/>
  </svg>

  <p class="block motto-small">&gt; Analyze &gt;&gt; Develop &gt;&gt;&gt; Deliver</p>
  <p class="block values">We are entrepreneurs.<br>
  &gt; We are committed to get things done.<br>
  &gt; We work closely with the client side by side.<br>
  &gt; We apply structured methods of reasoning.<br>
  &gt; We look at the problem from various angles.<br>
  &gt; We are not afraid of delivering unconventional solutions.<br>
  &gt; We analyze situations, develop solutions and implement results.</p>
  <p class="block registration">Valtorhaus AG is registered as a Swiss stock corporation since 1995.</p>

  <p class="block contact contact-address">Valtorhaus AG<br>Lindenhof-Strasse 14<br>CH-8052 Zürich</p>
  <p class="block contact contact-lines">Tel. +41 44 512 38 20<br>Fax. +41 44 512 38 21</p>
  <p class="block contact contact-web">www.valtorhaus.ch<br>info@valtorhaus.ch</p>

  <h1 class="block company-name">Valtorhaus AG</h1>
  <h2 class="block motto-large">Analyze &gt;&gt; Devlop &gt;&gt; Deliver</h2>
  <p class="block intro">We are a professional consulting, financing and<br>investment firm operating in the fields of:</p>
  <ul class="block services">
    <li>&gt; Project Development</li>
    <li>&gt; Management Consulting</li>
    <li>&gt; Investment Management</li>
    <li>&gt; Finance Solutions</li>
  </ul>
  <p class="block profile-label">COMPANY PROFILE</p>
</main>
</body>
</html>
```